Seed Oil Safety Card for Healthy Restaurant Dining

I am seeking a design for a physical card to communicate my wife's health-related dietary restriction regarding seed oils. This card will be given to restaurant waiters to ensure her meals are prepared without seed oils, as it is a health issue and not merely a preference.
My wife cannot eat any “seed oil” or “processed oil”, including:
- Vegetable oil
- Canola oil
- Soybean oil
- Sunflower oil
- Corn oil
- Cottonseed oil
- Safflower oil
- Peanut oil
- Sesame oil
Oils that are OK for her to consume:
- Butter (most preferable)
- Extra virgin olive oil
- Avocado oil
- Coconut oil
- Ghee
- Lard
- Any other animal-based fats
Key Design Requirements:
- Clarity and speed of communication: The card should be easily read and understood by waiters, even in low-light environments, emphasizing that it's a health concern.
- Avoid common misconceptions: Ensure the design doesn't imply common dietary preferences like "vegetarian" or "no butter." Animal fats and butter are actually preferable for her!
- Preferred term: Use "seed oils" as the term to describe what she cannot eat due to her health issue.
- Trace amounts are acceptable: Communicate that it's OK to use cookware that has previously been in contact with seed oils, but not to have seed oil as an ingredient. Please suggest a concise way to convey this.
- Card dimensions: Design should be 3.5” x 2.25” (standard credit-card size on cardlora-print.test). Horizontal or vertical layouts are both fine, whichever makes the message clearer.
Design Suggestions:
- Utilize bold and easy-to-read typography to communicate the main message.
- Consider incorporating relevant icons or graphics that help convey the message without adding confusion.
- Use contrasting colors to enhance readability, especially in low-light situations.
- To communicate the “trace amounts OK” part, consider phrases such as:
- "Cross-contamination acceptable"
- “Used cookware OK, no ingredient use”
- “Separate cookware not necessary”
Thank you for your assistance in creating this essential card for my wife's health and safety when dining out!

```html
<!DOCTYPE html>
<html lang="en">
<head>
<meta charset="utf-8">
<title>Seed Oil Safety Card</title>
<link rel="stylesheet" href="https://fonts.googleapis.com/css2?family=Roboto+Condensed:ital,wght@0,400;0,700;1,400&display=swap">
<style>
  :root {
    --page: #e0e0e0;
    --card: #052833;
    --white: #ffffff;
    --avoid: #e30613;
    --allow: #8fc21f;
  }
  * { margin: 0; padding: 0; box-sizing: border-box; }
  html, body {
    width: 1200px; height: 1200px; overflow: hidden;
    background: var(--page);
    font-family: "Roboto Condensed", "Arial Narrow", sans-serif;
  }
  .card {
    position: absolute; left: 297px; top: 102px;
    width: 601px; height: 933px;
    background: var(--card); border-radius: 38px;
  }
  .card > * { position: absolute; }
  .title {
    left: 0; right: 0; top: 146px;
    transform: translateY(-102px);
    text-align: center; color: var(--white);
    font-weight: 700; font-size: 37px; line-height: 39px;
    letter-spacing: 1.4px; text-transform: uppercase;
  }
  .icon { width: 72px; height: 72px; }
  .icon--avoid { left: 126px; top: 182px; }
  .icon--allow { left: 372px; top: 181px; }
  .heading {
    width: 260px; text-align: center; color: var(--white);
    font-weight: 700; font-size: 24.5px; line-height: 26px; letter-spacing: 1.3px;
  }
  .heading--avoid { left: 32px; top: 269px; }
  .heading--allow { left: 278px; top: 266px; }
  .pointer { width: 38px; height: 20px; }
  .pointer--avoid { left: 143px; top: 382px; }
  .pointer--allow { left: 389px; top: 379px; }
  .oil-list { list-style: none; font-size: 26px; line-height: 37.2px; letter-spacing: 0.6px; }
  .oil-list li { position: relative; padding-left: 27px; white-space: nowrap; }
  .oil-list li.bullet::before {
    content: ""; position: absolute; left: 0; top: 12px;
    width: 14px; height: 13px;
  }
  .oil-list--avoid { left: 62px; top: 420px; color: var(--avoid); }
  .oil-list--avoid li::before { background: var(--avoid); }
  .oil-list--allow { left: 322px; top: 420px; color: var(--allow); }
  .oil-list--allow li::before { background: var(--allow); top: 14px; }
  .cookware-note {
    left: 0; right: 0; top: 806px;
    text-align: center; color: var(--white);
    font-style: italic; font-size: 25px; line-height: 26px; letter-spacing: 1px;
  }
</style>
</head>
<body>
  <main class="card">
    <h1 class="title">My Wife's Health and Safety<br>When Dining Out!</h1>

    <svg class="icon icon--avoid" viewBox="0 0 72 72" aria-hidden="true">
      <rect x="2" y="2" width="68" height="68" rx="3" fill="none" stroke="var(--avoid)" stroke-width="4"/>
      <path d="M17 17 L55 55 M55 17 L17 55" stroke="var(--avoid)" stroke-width="10"/>
    </svg>
    <svg class="icon icon--allow" viewBox="0 0 72 72" aria-hidden="true">
      <rect x="2" y="2" width="68" height="68" rx="3" fill="none" stroke="var(--allow)" stroke-width="4"/>
      <path d="M16 36 L31 50 L56 17" fill="none" stroke="var(--allow)" stroke-width="10"/>
    </svg>

    <h2 class="heading heading--avoid">Cannot Eat<br>Any Seed Oil or<br>Processed Oil,<br>Including:</h2>
    <h2 class="heading heading--allow">Oils That<br>Are OK<br>For Her<br>To Consume:</h2>

    <svg class="pointer pointer--avoid" viewBox="0 0 38 20" aria-hidden="true"><path d="M0 0 H38 L19 20 Z" fill="var(--white)"/></svg>
    <svg class="pointer pointer--allow" viewBox="0 0 38 20" aria-hidden="true"><path d="M0 0 H38 L19 20 Z" fill="var(--white)"/></svg>

    <ul class="oil-list oil-list--avoid">
      <li class="bullet">Vegetable oil</li>
      <li class="bullet">Canola oil</li>
      <li class="bullet">Soybean oil</li>
      <li class="bullet">Sunflower oil</li>
      <li class="bullet">Corn oil</li>
      <li class="bullet">Cottonseed oil</li>
      <li class="bullet">Safflower oil</li>
      <li class="bullet">Peanut oil</li>
      <li class="bullet">Sesame oil</li>
    </ul>

    <ul class="oil-list oil-list--allow">
      <li class="bullet">Butter</li>
      <li>(most preferable)</li>
      <li class="bullet">Extra virgin</li>
      <li class="bullet">olive oil</li>
      <li class="bullet">Avocado oil</li>
      <li class="bullet">Coconut oil</li>
      <li class="bullet">Ghee</li>
      <li class="bullet">Lard</li>
      <li class="bullet">Any other</li>
      <li>animal-based fats</li>
    </ul>

    <p class="cookware-note">"Cross-contamination acceptable"<br>“Used cookware OK, no ingredient use"<br>“Separate cookware not necessary"</p>
  </main>
</body>
</html>
```